Office brochure for chronic pain doctor

I need an brochure for my office, and since I want to be able to mail the brochure, I think trifold would be the best size. I treat patients with chronic head and neck pain, as well as sleep apnea. I treat all of the following:

1. headaches
2. myofascial pain, which is a fancy way of saying muscle pain
3. neuropathic pain, which is a fancy way of saying nerve pain
4. TMJ, which stands for the temporomandibular joint (jaw joint)
5. obstructive sleep apnea

The colors will be based on my logo on my website, which you can see at www.BrightJPR.net, and you can learn more about what I do at my website. JPR stands for orofacial pain, which is a speciality training within the field of dentistry but I do not treat teeth. I have high resolution graphics for the brochure so I need someone with an artistic eye to design and lay out the brochure.

The logo colors are:
Purple 9e80bb
Pink f6b1d0
Blue 0f4b8f
Updates

I had a request for the logo in a .ai or .pdf format, which I have just uploaded. Please let me know if you have any other requests. Thank you, Dale

Target Market(s)

80% female, 20% male. I am in an upscale area of Los Angeles called Beverly Hills but I will see a patient from any area around Los Angeles or from any area in the world.

Industry/Entity Type

Training

Colors
6b449b
e567a6
0355a3

Requirements
Must have
• I want a small section of the brochure to feature each of the five areas I treat, and I have included an image to place in each of the five sections. A small section should include a short bio of me, which you can condense from www.brightjpr.net/dale. The brochure must appeal to women since 80% of my patients are female but I don't want to completely ignore men. Most of the pain patients are female, and most of the sleep apnea patients are male.

Here are the colors in my logo
Purple 9e80bb
Pink f6b1d0
Blue 0f4b8f
Should not have
• Anything related to teeth or dentistry.
No decorative or script fonts.

```html
<!DOCTYPE html>
<html lang="en">
<head>
<meta charset="utf-8">
<title>Dr. Dale Marwick – Trifold Brochure, Side 1</title>
<link rel="stylesheet" href="https://fonts.googleapis.com/css2?family=Source+Sans+3:wght@400;600;700&display=swap">
<style>
  :root{
    --brand-blue:#0f4b8f;
    --deep-blue:#0355a3;
    --brand-pink:#f6b1d0;
    --brand-purple:#9e80bb;
    --ink:#222222;
    --ink-soft:#4a4a4a;
    --paper:#ffffff;
    --stage:#e8e6e3;
  }
  *{margin:0;padding:0;box-sizing:border-box}
  html,body{width:1200px;height:918px;overflow:hidden;background:var(--stage)}
  body{font-family:"Source Sans 3",Arial,sans-serif;color:var(--ink)}
  .brochure{position:absolute;left:15px;top:4px;width:1170px;height:910px;background:var(--paper);overflow:hidden;box-shadow:0 2px 10px rgba(0,0,0,.18)}
  .photo{position:absolute}
  .photo--couple{left:0;top:0;width:394px;height:260px;background:linear-gradient(160deg,#e9e4df 0%,#c9b6a6 45%,#f1efed 100%)}
  .photo--neck{left:394px;top:0;width:381px;height:320px;background:linear-gradient(180deg,#eef1f3 0%,#c4d4e6 55%,#e6e6e6 100%)}
  .photo--headache{left:775px;top:0;width:395px;height:300px;background:linear-gradient(170deg,#5d7d3a 0%,#8da35d 40%,#e8cf9a 75%,#d9c7b0 100%)}
  .swoosh{position:absolute;left:0;top:0;width:1170px;height:910px}
  .panel{position:absolute;top:0;height:910px}
  .panel--flap{left:0;width:394px}
  .panel--back{left:394px;width:381px}
  .panel--front{left:775px;width:395px}

  .services-tab{position:absolute;left:0;top:292px;width:222px;height:36px;background:var(--brand-blue);clip-path:polygon(0 0,92% 0,100% 50%,92% 100%,0 100%);color:#fff;font-weight:600;font-size:22px;line-height:36px;padding-left:38px;letter-spacing:.2px}
  .services-list{position:absolute;left:37px;top:358px;list-style:none}
  .services-list li{display:flex;align-items:flex-start;font-size:19px;line-height:26px;margin-bottom:8.7px;font-weight:600;color:var(--ink)}
  .services-list svg{flex:0 0 15px;width:15px;height:15px;margin:6px 10px 0 0}
  .photo--patient{left:0;top:575px;width:394px;height:335px;background:linear-gradient(100deg,#cfe0b6 0%,#e8efdc 40%,#f6f3ee 75%,#ffffff 100%)}

  .bio-title{position:absolute;left:20px;width:341px;top:343px;text-align:center;color:var(--brand-blue);font-weight:700;font-size:19px;line-height:23px}
  .bio-text{position:absolute;left:26px;width:330px;font-size:12.4px;line-height:16.5px;text-align:justify;color:var(--ink-soft)}
  .bio-text--intro{top:409px}
  .bio-text--speaking{top:688px}
  .contact{position:absolute;left:24px;top:848px;white-space:nowrap;color:var(--ink-soft);font-size:22px}
  .contact strong{color:var(--brand-blue);font-size:32px;font-weight:700;margin-left:4px;vertical-align:-3px}

  .photo--portrait{left:45px;top:362px;width:306px;height:326px;background:radial-gradient(ellipse at 50% 55%,#dfe4ea 0%,#eef0f3 55%,#ffffff 80%)}
  .brand-mark{position:absolute;left:0;width:395px;top:712px;display:flex;align-items:center;justify-content:center;gap:14px}
  .brand-mark__square{width:58px;height:58px;background:var(--brand-purple)}
  .brand-mark__name{font-size:40px;font-weight:700;color:var(--brand-blue)}
  .tagline{position:absolute;left:0;width:395px;top:803px;text-align:center;font-weight:700;font-size:18px;color:var(--ink)}
  .doctor-name{position:absolute;left:0;width:395px;top:839px;text-align:center;font-weight:700;font-size:14.5px;color:var(--ink)}
  .doctor-address{position:absolute;left:20px;width:355px;top:862px;text-align:center;font-size:13.3px;line-height:18px;color:var(--ink)}
</style>
</head>
<body>
<main class="brochure">
  <div class="photo photo--couple" role="img" aria-label="Photo of a man snoring in bed while his partner covers her ears"></div>
  <div class="photo photo--neck" role="img" aria-label="Photo of a woman at her office desk holding her painful neck"></div>
  <div class="photo photo--headache" role="img" aria-label="Photo of a blonde woman holding her head with a headache"></div>

  <svg class="swoosh" viewBox="0 0 1170 910" aria-hidden="true">
    <path d="M0,121 C400,315 850,328 1170,192 L1170,245 C850,337 400,330 0,155 Z" fill="var(--brand-pink)"/>
    <path d="M0,155 C400,330 850,337 1170,245 L1170,301 C850,365 400,355 0,168 Z" fill="var(--brand-blue)"/>
    <path d="M0,168 C400,355 850,365 1170,301 L1170,910 L0,910 Z" fill="#ffffff"/>
  </svg>

  <section class="panel panel--flap">
    <h2 class="services-tab">OUR SERVICES</h2>
    <ul class="services-list">
      <li><svg viewBox="0 0 15 15"><rect x="0.75" y="0.75" width="13.5" height="13.5" fill="#fff" stroke="var(--brand-blue)" stroke-width="1.5"/><path d="M3 7.5 L6.3 10.8 L12.5 3.5" fill="none" stroke="var(--brand-blue)" stroke-width="2.4"/></svg>Headaches</li>
      <li><svg viewBox="0 0 15 15"><rect x="0.75" y="0.75" width="13.5" height="13.5" fill="#fff" stroke="var(--brand-blue)" stroke-width="1.5"/><path d="M3 7.5 L6.3 10.8 L12.5 3.5" fill="none" stroke="var(--brand-blue)" stroke-width="2.4"/></svg>Myofascial pain (muscle pain)</li>
      <li><svg viewBox="0 0 15 15"><rect x="0.75" y="0.75" width="13.5" height="13.5" fill="#fff" stroke="var(--brand-blue)" stroke-width="1.5"/><path d="M3 7.5 L6.3 10.8 L12.5 3.5" fill="none" stroke="var(--brand-blue)" stroke-width="2.4"/></svg>Neuropathic pain, (nerve pain)</li>
      <li><svg viewBox="0 0 15 15"><rect x="0.75" y="0.75" width="13.5" height="13.5" fill="#fff" stroke="var(--brand-blue)" stroke-width="1.5"/><path d="M3 7.5 L6.3 10.8 L12.5 3.5" fill="none" stroke="var(--brand-blue)" stroke-width="2.4"/></svg><span>TMJ, which stands for the<br>temporomandibular joint (jaw joint)</span></li>
      <li><svg viewBox="0 0 15 15"><rect x="0.75" y="0.75" width="13.5" height="13.5" fill="#fff" stroke="var(--brand-blue)" stroke-width="1.5"/><path d="M3 7.5 L6.3 10.8 L12.5 3.5" fill="none" stroke="var(--brand-blue)" stroke-width="2.4"/></svg>Obstructive sleep apnea</li>
    </ul>
    <div class="photo photo--patient" role="img" aria-label="Photo of an older woman resting her aching jaw in her hand"></div>
  </section>

  <section class="panel panel--back">
    <h1 class="bio-title">Dr. Dale Marwick Beverly Hills<br>Facial Pain Doctor</h1>
    <p class="bio-text bio-text--intro">I have lived in Beverly Hills since 1993, I wanted to practice locally, and was fortunate to find a great location at the corner of Alder Way and Kestrel Drive, in the Golden Triangle building, which is where Casa Luna is. It is a great building, and I have tried to create a unique office to help patients suffering from chronic head and neck pain. If you are suffering from migraine headaches, cluster headaches, morning headaches, head and neck muscle pain, sharp shooting electrical type of pain in your head or neck, TMJ (or what you have been told is TMJ), or snoring and/or obstructive sleep apnea, please make an appointment at my Beverly Hills chronic pain office for me to examine you to see if I can help manage or eliminate your pain. I promise, I will not even consider drilling your teeth or intentionally try to change your bite to help reduce your pain!</p>
    <p class="bio-text bio-text--speaking">If you are a dentist, and are interesting in hearing me speak, please know that I have presented at small study clubs, local dental societies, and annual state dental association meetings, and from groups as small as 20 to an audience as large as 2.000. Here are some good testimonials to read from other dentists so please let me know if you are interested in hearing me speak. I guarantee that I will make you think!</p>
    <p class="contact">CONTACT ME: <strong>888.555.0142</strong></p>
  </section>

  <section class="panel panel--front">
    <div class="photo photo--portrait" role="img" aria-label="Portrait photo of Dr. Dale Marwick in a white coat"></div>
    <div class="brand-mark">
      <span class="brand-mark__square"></span>
      <span class="brand-mark__name">Bright JPR</span>
    </div>
    <p class="tagline">Caring for Head Pain and Sleep Apnea</p>
    <p class="doctor-name">Dale Marwick, DDS, MBA</p>
    <p class="doctor-address">Diplomate National Board of Head Pain Care, 4820 Alder<br>Way, Suite 210, Beverly Hills, CA 90210</p>
  </section>
</main>
</body>
</html>
```